KELP clinical trial results infographic

We need an infographic which presents the results from the KELP research trial. It should be colourful and engaging, in understandable language and showing the steps to get to the results. This is to showcase the results to patients/the public/clinicians, giving a brief summary of what the study proved. The final design should have the KELP logo at the top (please see the logo on the attached Word document)
I have attached the required logos which need to be used (KELP - within the Word doc, Brindlemoor Injury and Acute Care, University of Caddering, QRV - see also their design pack attached) as well as an example from another study, PLUMBEX4, as an example of what the layout could look like. Please DO NOT use the content from the PLUMBEX4 example though, please instead use the content from the attached document 'InfographicDesignInformation_KELP_ArtHatchery_02Dec2025'. Please also include information about the funding in a footer at the bottom of the infographic (as per the above document).
Look and feel
Each slider illustrates characteristics of the customer's brand and the style your logo design should communicate.

```html
<!DOCTYPE html>
<html lang="en">
<head>
<meta charset="utf-8">
<title>KELP trial results</title>
<link rel="stylesheet" href="https://fonts.googleapis.com/css2?family=Poppins:wght@400;500;600;700;800&display=swap">
<style>
:root{
  --navy:#0d2a5c;
  --navy-deep:#08234f;
  --blue:#1b4f9c;
  --band:#2d79c1;
  --sky:#d6e8fa;
  --tick:#2f7fd0;
  --gold:#f2c12e;
  --ink:#1c1c1c;
  --rule:#5a6f95;
  --orange:#f0a21f;
  --red:#c4283a;
  --grey:#6d6d6d;
}
*{margin:0;padding:0;box-sizing:border-box}
html,body{width:863px;height:1200px;overflow:hidden;background:#fff}
body{font-family:'Poppins',sans-serif;color:var(--ink);position:relative}
.abs{position:absolute}
ul{list-style:none}
.tick{flex:none;width:9px;height:9px;margin-top:3px}

/* header */
.brand-kelp{left:51px;top:36px;font-size:60px;font-weight:800;color:var(--blue);letter-spacing:1px;line-height:1}
.brand-uni{left:702px;top:0;width:108px;height:120px;background:var(--navy);display:flex;align-items:flex-end;justify-content:center;padding:0 8px 14px;text-align:center;color:#fff;font-size:11px;font-weight:500;line-height:1.25;text-transform:uppercase;letter-spacing:.5px}
.headline{left:0;top:134px;width:863px;text-align:center;font-weight:800;font-size:34px;line-height:37px}
.headline .l1{color:var(--navy);display:block}
.headline .l2{color:var(--blue);display:block}

/* summary band */
.band{left:0;top:200px;width:863px;height:278px}
.summary{left:50px;top:260px;color:#fff}
.summary h2{font-size:23.5px;font-weight:700;line-height:30px;margin-bottom:1px}
.summary p{font-size:11.3px;line-height:14.3px;margin-bottom:8px}
.summary .p1{width:480px}
.summary .p2{width:530px}
.summary .p3{width:500px}
.ankle-art{left:616px;top:272px;width:172px;height:172px;border-radius:50%;border:5px solid #fff;background:radial-gradient(circle at 50% 45%,#fbe8d4 0%,#f3c79e 35%,#c7e7e3 62%,#c4e3e0 100%)}

/* key messages */
.key h2{position:absolute;left:51px;top:488px;font-size:24px;font-weight:700;color:var(--blue);line-height:30px}
.key li{position:absolute;top:523px;font-size:11.6px;line-height:15px;display:flex;gap:9px}
.key .tick{width:11px;height:11px;margin-top:2px}
.dash{left:46px;width:775px;border-top:1.3px dashed var(--rule)}

/* eligibility */
.elig-tab{left:290px;top:580px;width:283px;height:31px}
.elig-title{left:290px;top:580px;width:283px;height:31px;display:flex;align-items:center;justify-content:center;color:#fff;font-weight:700;font-size:23px}
.elig-box{left:51px;top:611px;width:762px;height:206px;border:1.2px solid #7a8fb0}
.crit{top:629px}
.crit h3{font-size:17px;font-weight:700;color:var(--navy);line-height:22px;margin-bottom:5px}
.crit li{font-size:11.6px;line-height:15px;display:flex;gap:9px;margin-bottom:8px}
.crit b{font-weight:700}
.crit.inc{left:73px;width:360px}
.crit.exc{left:481px;width:320px}
.crit.inc li{padding-left:6px}
.col-split{left:440px;top:640px;height:160px;border-left:1.2px dashed var(--rule)}

/* study details */
.details{left:0;top:817px;width:863px;height:244px;background:var(--sky)}
.details h2{position:absolute;left:51px;top:8px;font-size:24px;font-weight:700;color:var(--blue);line-height:30px}
.people-art{left:54px;top:864px;width:150px;height:130px;border-radius:10px 10px 50% 50%/10px 10px 14px 14px;background:linear-gradient(180deg,#b9d3ef 0%,#4c78b5 60%,#9aa2ad 100%)}
.hospital-art{left:294px;top:850px;width:200px;height:137px;background:linear-gradient(180deg,#2b4f8c 0%,#1f3d70 70%,#4f9a3a 100%);border-radius:3px}
.cap{text-align:center;font-size:12.5px;line-height:15px}
.cap.rct{left:44px;top:1013px;width:160px}
.cap.hosp{left:247px;top:997px;width:240px}
.cap.hosp strong{display:block;color:var(--blue);font-size:17.5px;font-weight:700;line-height:20px}
.vsplit{top:877px;height:160px;border-left:1.2px dashed var(--rule)}
.panel{left:550px;top:854px;width:313px;height:161px;background:var(--navy-deep);border-radius:27px 0 0 27px;padding:34px 12px 0 22px;color:#fff}
.panel li{font-size:11.6px;line-height:15px;display:flex;gap:10px;margin-bottom:12px}
.panel em{font-style:normal;color:var(--gold);font-weight:600}

/* footer */
.funding{left:40px;top:1074px;width:783px;text-align:center;font-size:12px;line-height:16px}
.partner-qrv{left:51px;top:1136px;display:flex;align-items:center;gap:12px}
.partner-qrv .mark{width:37px;height:37px;background:var(--orange)}
.partner-qrv .name{font-size:20px;font-weight:500;color:var(--navy)}
.contact{left:223px;top:1138px;width:273px;height:62px;background:var(--navy-deep);border-radius:20px 20px 0 0;display:flex;justify-content:center;padding-top:14px;gap:8px;color:#fff;font-size:12.5px;line-height:16px}
.contact svg{margin-top:4px}
.partner-bac{left:526px;top:1154px;display:flex;align-items:center;gap:6px}
.partner-bac .mark{width:13px;height:13px;border-radius:50%;background:var(--red)}
.partner-bac .name{font-size:11px;color:var(--grey);text-transform:uppercase;white-space:nowrap}
</style>
</head>
<body>

<!-- header -->
<div class="abs brand-kelp">KELP</div>
<div class="abs brand-uni">University of Caddering</div>
<h1 class="abs headline"><span class="l1">PATIENTS CAN SAFELY START WALKING</span><span class="l2">SOON AFTER SURGERY ON A BROKEN ANKLE.</span></h1>

<!-- summary band -->
<svg class="abs band" viewBox="0 0 863 278" aria-hidden="true">
  <rect x="0" y="0" width="863" height="278" fill="var(--band)"/>
  <path d="M0 14 C150 32 300 46 440 46 C560 46 700 30 863 4 L863 2 C650 22 500 30 420 30 C250 30 120 22 0 10 Z" fill="var(--navy)"/>
  <path d="M0 0 H863 V2 C650 22 500 30 420 30 C250 30 120 22 0 10 Z" fill="#fff"/>
</svg>

<section class="abs summary">
  <h2>STUDY SUMMARY</h2>
  <p class="p1">Ankle fractures are very common, and often require an operation. After surgery for ankle fracture, patients are usually advised to avoid walking for 6 weeks (delayed weight-bearing).</p>
  <p class="p2">An alternative is to walk 2 weeks after surgery (early weight-bearing). In this study,half of the patients were instructed that they should put as much weight through their affected leg as they felt comfortable and without causing pain. The other half were instructed to avoid putting any weight through their operated leg for six weeks after surgery.</p>
  <p class="p3">After 4 months, ankle function was similar, and the number of complications was similar, in the two groups. The cost to the NHC and social services were also similar, with slightly lower costs in the early weight-bearing group.</p>
</section>
<div class="abs ankle-art" role="img" aria-label="Illustration of a foot and ankle skeleton with the painful fracture area highlighted"></div>

<!-- key messages -->
<section class="key">
  <h2>KEY MESSAGES</h2>
  <ul>
    <li style="left:56px;width:370px"><svg class="tick" viewBox="0 0 12 12"><circle cx="6" cy="6" r="6" fill="var(--navy)"/><path d="M3.3 6.2l1.8 1.8 3.6-3.8" stroke="#fff" stroke-width="1.5" fill="none"/></svg><span>An early weight-bearing strategy is not inferior in terms<br>of ankle function to a delayed weight-bearing strategy.</span></li>
    <li style="left:459px;width:300px"><svg class="tick" viewBox="0 0 12 12"><circle cx="6" cy="6" r="6" fill="var(--navy)"/><path d="M3.3 6.2l1.8 1.8 3.6-3.8" stroke="#fff" stroke-width="1.5" fill="none"/></svg><span>Early weight-bearing is also likely to<br>be cost-effective.</span></li>
  </ul>
</section>

<div class="abs dash" style="top:570px"></div>

<!-- eligibility -->
<svg class="abs elig-tab" viewBox="0 0 283 31" aria-hidden="true">
  <path d="M12 0 H271 L283 31 H0 Z" fill="var(--navy)"/>
</svg>
<div class="abs elig-title">ELIGIBILITY CRITERIA</div>
<div class="abs elig-box"></div>

<section class="abs crit inc">
  <h3>INCLUSION CRITERIA:</h3>
  <ul>
    <li><svg class="tick" viewBox="0 0 12 12"><circle cx="6" cy="6" r="6" fill="var(--tick)"/><path d="M3.3 6.2l1.8 1.8 3.6-3.8" stroke="#fff" stroke-width="1.6" fill="none"/></svg><span><b>Aged 18</b> or over</span></li>
    <li><svg class="tick" viewBox="0 0 12 12"><circle cx="6" cy="6" r="6" fill="var(--tick)"/><path d="M3.3 6.2l1.8 1.8 3.6-3.8" stroke="#fff" stroke-width="1.6" fill="none"/></svg><span>Has had operative fixation for an<br><b>unstable ankle fracture.</b></span></li>
    <li><svg class="tick" viewBox="0 0 12 12"><circle cx="6" cy="6" r="6" fill="var(--tick)"/><path d="M3.3 6.2l1.8 1.8 3.6-3.8" stroke="#fff" stroke-width="1.6" fill="none"/></svg><span>Surgery was performed within <b>14 days of the injury.</b></span></li>
    <li><svg class="tick" viewBox="0 0 12 12"><circle cx="6" cy="6" r="6" fill="var(--tick)"/><path d="M3.3 6.2l1.8 1.8 3.6-3.8" stroke="#fff" stroke-width="1.6" fill="none"/></svg><span>The treating surgeon considers that the participant<br>might <b>benefit from early weight-bearing.</b></span></li>
    <li><svg class="tick" viewBox="0 0 12 12"><circle cx="6" cy="6" r="6" fill="var(--tick)"/><path d="M3.3 6.2l1.8 1.8 3.6-3.8" stroke="#fff" stroke-width="1.6" fill="none"/></svg><span><b>Able and willing</b> to give informed consent</span></li>
  </ul>
</section>

<div class="abs col-split"></div>

<section class="abs crit exc">
  <h3>EXCLUSION CRITERIA:</h3>
  <ul>
    <li><svg class="tick" viewBox="0 0 12 12"><circle cx="6" cy="6" r="6" fill="var(--tick)"/><path d="M3.3 6.2l1.8 1.8 3.6-3.8" stroke="#fff" stroke-width="1.6" fill="none"/></svg><span>A lack of <b>protective sensation</b> (e.g. peripheral<br>neuropathy).</span></li>
    <li><svg class="tick" viewBox="0 0 12 12"><circle cx="6" cy="6" r="6" fill="var(--tick)"/><path d="M3.3 6.2l1.8 1.8 3.6-3.8" stroke="#fff" stroke-width="1.6" fill="none"/></svg><span><b>Inability to adhere</b> to trial procedures.</span></li>
    <li><svg class="tick" viewBox="0 0 12 12"><circle cx="6" cy="6" r="6" fill="var(--tick)"/><path d="M3.3 6.2l1.8 1.8 3.6-3.8" stroke="#fff" stroke-width="1.6" fill="none"/></svg><span><b>Bilateral operatively</b> treated ankle fractures.</span></li>
    <li><svg class="tick" viewBox="0 0 12 12"><circle cx="6" cy="6" r="6" fill="var(--tick)"/><path d="M3.3 6.2l1.8 1.8 3.6-3.8" stroke="#fff" stroke-width="1.6" fill="none"/></svg><span>Already in a trial for <b>ankle fracture.</b></span></li>
    <li><svg class="tick" viewBox="0 0 12 12"><circle cx="6" cy="6" r="6" fill="var(--tick)"/><path d="M3.3 6.2l1.8 1.8 3.6-3.8" stroke="#fff" stroke-width="1.6" fill="none"/></svg><span>Patient has received a <b>hindfoot nail to treat<br>index fracture.</b></span></li>
  </ul>
</section>

<!-- study details -->
<section class="abs details"><h2>STUDY DETAILS</h2></section>
<div class="abs people-art" role="img" aria-label="Illustration of a group of four adult trial participants standing together"></div>
<div class="abs cap rct">Randomised<br>controlled trial</div>
<div class="abs vsplit" style="left:241px"></div>
<div class="abs hospital-art" role="img" aria-label="Illustration of a hospital building with trees"></div>
<div class="abs cap hosp"><strong>561 ADULTS</strong>recruited from <b>23 NHC hospitals</b><br>in the UK</div>
<div class="abs vsplit" style="left:517px"></div>

<div class="abs panel">
  <ul>
    <li><svg class="tick" viewBox="0 0 12 12"><circle cx="6" cy="6" r="6" fill="var(--gold)"/><path d="M3.3 6.2l1.8 1.8 3.6-3.8" stroke="var(--navy-deep)" stroke-width="1.6" fill="none"/></svg><span>A non-inferiority study</span></li>
    <li><svg class="tick" viewBox="0 0 12 12"><circle cx="6" cy="6" r="6" fill="var(--gold)"/><path d="M3.3 6.2l1.8 1.8 3.6-3.8" stroke="var(--navy-deep)" stroke-width="1.6" fill="none"/></svg><span>Ankle function, quality of life and<br>complications were collected at<br><em>6 weeks, 4 months and<br>12 months</em> after surgery.</span></li>
  </ul>
</div>

<!-- footer -->
<div class="abs dash" style="top:1061px"></div>
<p class="abs funding">National Institute for Clinical Studies, Patient Outcomes Fund (PO-RG-0419-31752), supported by<br>the NICS Caddering Biomedical Research Centre</p>

<div class="abs partner-qrv"><span class="mark"></span><span class="name">QRV</span></div>

<div class="abs contact">
  <svg width="13" height="9" viewBox="0 0 12 9" aria-hidden="true"><rect x=".6" y=".6" width="10.8" height="7.8" fill="none" stroke="var(--gold)" stroke-width="1.1"/><path d="M.8 .8L6 5l5.2-4.2" fill="none" stroke="var(--gold)" stroke-width="1.1"/></svg>
  <span>hello@qrv-health.org</span>
</div>

<div class="abs partner-bac"><span class="mark"></span><span class="name">Brindlemoor Injury and Acute Care</span></div>

</body>
</html>
```